Postcard Design

I am a mortgage broker located in Michigan. I recently opened my own company after working for another for 7 years. I want to send out a mailing letting my old clients know my new information and also reach out to them to let me know if I can assist them with anything.

It Company

```html
<!DOCTYPE html>
<html lang="en">
<head>
<meta charset="utf-8">
<title>Lakeshore Mortgage Postcard</title>
<link rel="stylesheet" href="https://fonts.googleapis.com/css2?family=Oswald:wght@500&family=Montserrat:wght@500&family=Roboto:wght@400&display=swap">
<style>
  :root {
    --paper: #ffffff;
    --brand-blue: #1f62a6;
    --name-blue: #1d5283;
    --band-light: #3a8fd0;
    --band-dark: #1b6bab;
    --contact-text: #ffffff;
    --photo-top: #c9a089;
    --photo-mid: #6b6f78;
    --photo-bottom: #1f2b3e;
  }
  html, body {
    margin: 0;
    padding: 0;
    overflow: hidden;
    background: var(--paper);
  }
  .postcard {
    position: relative;
    width: 1200px;
    height: 929px;
    background: var(--paper);
    overflow: hidden;
  }
  .brand {
    position: absolute;
    left: 700px;
    top: 200px;
    width: 440px;
    display: flex;
    align-items: center;
    justify-content: center;
    gap: 16px;
  }
  .brand-mark {
    width: 22px;
    height: 22px;
    background: var(--brand-blue);
  }
  .brand-name {
    font-family: "Oswald", sans-serif;
    font-weight: 500;
    font-size: 48px;
    letter-spacing: 1px;
    color: var(--brand-blue);
    line-height: 1;
  }
  .contact-band {
    position: absolute;
    left: 390px;
    top: 471px;
    width: 765px;
    height: 429px;
    background: linear-gradient(100deg, var(--band-light) 0%, var(--band-dark) 100%);
  }
  .portrait {
    position: absolute;
    left: 36px;
    top: 165px;
    width: 534px;
    height: 735px;
    background: linear-gradient(180deg, var(--photo-top) 0%, var(--photo-mid) 45%, var(--photo-bottom) 100%);
  }
  .owner-name {
    position: absolute;
    right: 45px;
    top: 400px;
    margin: 0;
    font-family: "Montserrat", sans-serif;
    font-weight: 500;
    font-size: 52px;
    letter-spacing: 4px;
    color: var(--name-blue);
    line-height: 1;
  }
  .contact-list {
    position: absolute;
    right: 69px;
    top: 534px;
    margin: 0;
    padding: 0;
    list-style: none;
    text-align: right;
    font-family: "Roboto", sans-serif;
    font-size: 35px;
    color: var(--contact-text);
    line-height: 60px;
  }
  .contact-list .address {
    margin-top: 20px;
    line-height: 54px;
    letter-spacing: 1px;
  }
</style>
</head>
<body>
  <main class="postcard">
    <div class="brand">
      <span class="brand-mark"></span>
      <span class="brand-name">LAKESHORE MORTGAGE</span>
    </div>

    <div class="contact-band"></div>

    <div class="portrait" role="img" aria-label="Portrait photograph of the broker in a dark suit and tie"></div>

    <h1 class="owner-name">OWNER NAME</h1>

    <ul class="contact-list">
      <li>FAX :(000) 000 000</li>
      <li>OFFICE : (000) 000 000</li>
      <li>CALL : 1(000) 000 000</li>
      <li>E-MAIL : ab34@example.com</li>
      <li class="address">ADDRESS : 5555, AAAA,<br>AAAAAAASD.</li>
    </ul>
  </main>
</body>
</html>
```